Pest Control Company needs business card!

Hi there, we need a business card designed for our new Pest Control Company. Ideally this card will be simple, yet feel elegant and high end. We want to use the colours Orange, Black and White. Please see our attached logo for the exact colours.

Business card details:

Phone - 0438 517 264
Name - Gus Halloran
Email - Info@trueguardpest.com.au

We would also like to include the following list with dot points:

SERVICES / INSPECTIONS

Termites, Wood Borers, Ants, Cockroaches, Spiders, Fleas, Mice, Rats, Bed Bugs, & More!

```html
<!DOCTYPE html>
<html lang="en">
<head>
<meta charset="utf-8">
<title>TrueGuard Pest Control – Business Card</title>
<link href="https://fonts.googleapis.com/css2?family=Arimo:wght@400;700&display=swap" rel="stylesheet">
<style>
  :root {
    --backdrop: #d8d6d7;
    --card-white: #ffffff;
    --card-black: #222021;
    --ink: #1e1c1d;
    --accent-red: #e32b1f;
    --soft-white: #d9d7d8;
  }
  * { margin: 0; padding: 0; box-sizing: border-box; }
  html, body {
    width: 1200px; height: 1100px; overflow: hidden;
    background: var(--backdrop);
    font-family: "Arimo", Arial, sans-serif;
  }
  .card {
    position: absolute; left: 259px; width: 705px; height: 405px;
    box-shadow: 0 1px 4px rgba(0,0,0,0.35);
  }
  .card-front { top: 115px; background: var(--card-white); color: var(--ink); }
  .card-back  { top: 560px; background: var(--card-black); color: var(--card-white); }

  .brand-name {
    font-family: "Arimo", Arial, sans-serif;
    font-weight: 700;
    text-transform: uppercase;
    letter-spacing: 0.3px;
    white-space: nowrap;
  }
  .card-front .brand-name {
    position: absolute; left: 46px; top: 84px;
    font-size: 26px; color: var(--ink);
  }

  .holder {
    position: absolute; right: 38px; top: 80px; text-align: right;
  }
  .holder-name {
    font-weight: 700; font-size: 24px; letter-spacing: 0.3px;
    text-transform: uppercase; color: var(--ink);
  }
  .holder-title {
    font-size: 18px; color: var(--accent-red); margin-top: 2px;
  }

  .contact-list {
    position: absolute; left: 42px; top: 288px; list-style: none;
    font-size: 16px; color: var(--ink);
  }
  .contact-list li {
    display: flex; align-items: center; height: 23px;
  }
  .contact-list svg {
    width: 13px; height: 13px; margin-right: 5px; flex: none;
    fill: var(--accent-red); stroke: var(--accent-red);
  }

  .card-back .brand-name {
    position: absolute; left: 0; right: 0; top: 92px;
    text-align: center; font-size: 38px; color: var(--card-white);
  }
  .services {
    position: absolute; left: 0; right: 0; top: 176px; text-align: center;
  }
  .services-title {
    font-weight: 700; font-size: 16px; letter-spacing: 2px;
    color: var(--accent-red); text-transform: uppercase;
  }
  .services-list {
    list-style: none; margin: 20px auto 0; width: 460px;
    display: grid; grid-template-columns: repeat(3, 1fr);
    row-gap: 10px; column-gap: 16px; text-align: left;
    font-size: 15px; color: var(--soft-white);
  }
  .services-list li { display: flex; align-items: center; }
  .services-list li::before {
    content: ""; width: 6px; height: 6px; border-radius: 50%;
    background: var(--accent-red); margin-right: 9px; flex: none;
  }
</style>
</head>
<body>

<section class="card card-front">
  <h1 class="brand-name">TrueGuard Pest Control</h1>

  <div class="holder">
    <p class="holder-name">Gus Halloran</p>
    <p class="holder-title">President</p>
  </div>

  <ul class="contact-list">
    <li>
      <svg viewBox="0 0 16 16" aria-hidden="true"><path stroke="none" d="M3.6 1.2l2.3 2.6c.4.4.3 1-.1 1.4L4.6 6.3c.9 2.2 2.7 4 4.9 4.9l1.1-1.2c.4-.4 1-.5 1.4-.1l2.6 2.3c.4.4.4 1 0 1.4l-1.4 1.4c-.6.6-1.5.8-2.3.5C5.9 13.8 2.2 10.1.5 5.1.2 4.3.4 3.4 1 2.8L2.2 1.2c.4-.4 1-.4 1.4 0z"/></svg>
      0438 517 264
    </li>
    <li>
      <svg viewBox="0 0 16 16" aria-hidden="true"><rect x="0.5" y="3" width="15" height="10" stroke="none"/><path d="M1 3.5l7 5.5 7-5.5M1 12.5l5-4.5M15 12.5l-5-4.5" fill="none" stroke="#fff" stroke-width="1.2"/></svg>
      Info@trueguardpest.com.au
    </li>
    <li>
      <svg viewBox="0 0 16 16" aria-hidden="true" fill="none"><g fill="none" stroke-width="1.3"><circle cx="8" cy="8" r="6.8"/><ellipse cx="8" cy="8" rx="3" ry="6.8"/><path d="M1.2 8h13.6M2.3 4.6h11.4M2.3 11.4h11.4"/></g></svg>
      www.trueguardpest.com.au
    </li>
  </ul>
</section>

<section class="card card-back">
  <h2 class="brand-name">TrueGuard Pest Control</h2>

  <div class="services">
    <p class="services-title">Services / Inspections</p>
    <ul class="services-list">
      <li>Termites</li>
      <li>Wood Borers</li>
      <li>Ants</li>
      <li>Cockroaches</li>
      <li>Spiders</li>
      <li>Fleas</li>
      <li>Mice</li>
      <li>Rats</li>
      <li>Bed Bugs</li>
      <li>&amp; More!</li>
    </ul>
  </div>
</section>

</body>
</html>
```